New website for our Escape Room

We are wanting to create a new website for our website. We have 2 different locations that guests will choose their location on the home page. Then we have 5 different escape room experiences. We like clean and fresh but fun. Our logo is black white and red. We like a modern feel that is simple to navigate. I love movement on the page. You can see our current site at quillhornpuzzles.com
We like fresh and modern. It needs to include much of the same information as out current site but we won't like the look of our site.

Target Market(s)

amusement, escape rooms.

Industry/Entity Type

escape room

Number of Pages Required

4 page

Requirements
Must have
• info on all 4 escape rooms, option to choose between Pigeon Forge and Nashville locations.

```html
<!DOCTYPE html>
<html lang="en">
<head>
<meta charset="utf-8">
<title>Quillhorn Escape Game</title>
<link href="https://fonts.googleapis.com/css2?family=Oswald:wght@400;500;600;700&family=Lato:wght@400;700;900&display=swap" rel="stylesheet">
<style>
:root{
  --red:#e3000f;
  --black:#050505;
  --navy:#141826;
  --navy-2:#1b2030;
  --white:#ffffff;
}
*{box-sizing:border-box;margin:0;padding:0}
html,body{width:1200px;height:5093px;overflow:hidden;background:var(--black)}
body{position:relative;font-family:'Lato',sans-serif;color:var(--white)}
.abs{position:absolute}
.head{font-family:'Oswald',sans-serif;font-weight:600;text-transform:uppercase;letter-spacing:.5px;white-space:nowrap}
.center{text-align:center}
.btn{position:absolute;display:flex;align-items:center;justify-content:center;background:var(--red);color:#fff;font-family:'Oswald',sans-serif;font-weight:500;font-size:12px;text-transform:uppercase;letter-spacing:.5px}
.btn::after{content:"";position:absolute;right:-10px;top:-2px;bottom:-2px;width:8px;border:2px solid var(--red);border-left:none}
.brand{font-family:'Oswald',sans-serif;font-weight:500;color:#fff;display:flex;align-items:center;gap:10px;text-transform:uppercase;white-space:nowrap}
.brand i{display:block;background:var(--red)}

.site-header{left:0;top:0;width:1200px;height:120px;z-index:2}
.nav{left:395px;top:50px;display:flex;gap:22px;font-family:'Oswald',sans-serif;font-size:12px;text-transform:uppercase}
.nav .active{color:var(--red)}
.hero{left:0;top:0;width:1200px;height:700px;background:radial-gradient(ellipse at 50% 35%,#3a3a3a 0%,#1a1a1a 40%,#050505 80%)}
.hero-title{left:0;top:210px;width:1200px;font-family:'Oswald',sans-serif;font-weight:500;font-size:170px;line-height:1;color:#a0a0a0;letter-spacing:2px}
.hero-tag{left:0;top:438px;width:1200px;font-family:'Oswald',sans-serif;font-weight:400;font-size:30px;letter-spacing:14px;color:#fff;text-transform:uppercase;white-space:nowrap}
.about-img{left:200px;top:680px;width:380px;height:360px;background:radial-gradient(ellipse at 50% 40%,#4a3a30,#151212 60%,#050505)}
.about h2{left:613px;top:735px;font-size:52px}
.about p{left:613px;top:828px;width:420px;font-size:13.5px;line-height:26px;color:#e8e8e8}
.rooms{left:0;top:1150px;width:1200px;height:720px;background:linear-gradient(#050505,#101010 50%,#050505)}
.section-title{font-size:54px}
.room{width:265px;height:207px}
.room .shot{position:absolute;left:22px;top:10px;right:0;bottom:10px;display:flex;align-items:center;justify-content:center;font-family:'Oswald',sans-serif;font-size:34px;font-weight:600;text-transform:uppercase;letter-spacing:1px;white-space:nowrap}
.room svg{position:absolute;left:0;top:0}
.price{width:265px;height:370px;background:linear-gradient(#c40010 0%,#9b0009 20%,#2f2f2f 32%,#3c3c3c 60%,#1d1d1d 100%)}
.price .tier{position:absolute;top:14px;width:100%;text-align:center;font-family:'Oswald',sans-serif;font-size:19px;font-weight:500}
.price .amt{position:absolute;top:42px;width:100%;text-align:center;font-family:'Oswald',sans-serif;font-size:28px;font-weight:600}
.price ul{position:absolute;top:110px;width:100%;list-style:none;text-align:center;font-size:14px;line-height:33.5px;color:#e6e6e6}
.price ul li:first-child{font-weight:900;font-size:16px}
.benefits{left:0;top:2877px;width:1200px;height:722px;background:var(--navy)}
.benefit{width:150px;height:250px}
.benefit .label{position:absolute;top:60px;width:100%;text-align:center;font-family:'Oswald',sans-serif;font-size:11px;letter-spacing:1px;text-transform:uppercase;line-height:16px}
.benefit .label b{display:block;font-weight:600;font-size:12px;letter-spacing:0}
.locations{left:0;top:3599px;width:1200px;height:600px;background:radial-gradient(ellipse at 50% 50%,#2a2a2a,#0a0a0a 70%)}
.loc{width:420px;display:flex;flex-direction:column;align-items:center}
.loc .brand{font-size:58px;line-height:1}
.loc .city{font-family:'Oswald',sans-serif;font-weight:400;font-size:20px;letter-spacing:2px;text-transform:uppercase;margin-top:14px;color:#fff}
.loc p{font-size:14px;line-height:26px;text-align:center;margin-top:8px;font-weight:700}
.who-panel{left:175px;top:4190px;width:1025px;height:395px;background:var(--navy-2)}
.who-item{width:230px;text-align:center}
.who-item h4{font-family:'Oswald',sans-serif;font-weight:500;font-size:18px;margin-top:12px;text-transform:uppercase}
.who-item p{font-size:14px;line-height:25px;color:#e5e5e5;margin-top:4px}
.icon-badge{width:100px;height:100px;margin:0 auto;background:var(--red);border-radius:10px 34px 10px 10px;display:flex;align-items:center;justify-content:center}
.footer{left:0;top:4640px;width:1200px;height:453px;background:linear-gradient(#0a0a0a,#121212)}
.f-title{font-family:'Oswald',sans-serif;font-size:17px;font-weight:500}
.f-title span{color:var(--red)}
.f-links{font-size:12px;line-height:37px;color:#d5d5d5;font-family:'Oswald',sans-serif;text-transform:uppercase;list-style:none}
.f-contact{font-size:12.5px;color:#d5d5d5;line-height:20px}
.f-contact div{display:flex;gap:10px;margin-bottom:17px}
.f-contact svg{flex:none;margin-top:3px}
.social{width:22px;height:22px;border:2px solid var(--red);border-left:none;display:flex;align-items:center;justify-content:center;font-size:11px;font-weight:900}
</style>
</head>
<body>

<section class="hero abs" role="img" aria-label="Dim stone prison cell with a barred window"></section>

<header class="site-header abs">
  <div class="brand abs" style="left:174px;top:36px;font-size:40px"><i style="width:10px;height:10px"></i>Quillhorn</div>
  <nav class="nav abs">
    <span class="active">Home</span><span>About Us</span><span>Escape Rooms</span><span>FAQ</span><span>Gallery</span><span>Gift Cards</span><span>Contact</span>
  </nav>
  <div class="btn" style="left:872px;top:44px;width:146px;height:34px">Find Your Location</div>
</header>

<div class="hero-title abs center">QUILLHORN</div>
<div class="hero-tag abs center">Escape Rooms for Every Party</div>
<svg class="abs" style="left:586px;top:582px" width="28" height="44" viewBox="0 0 28 44"><rect x="2" y="2" width="24" height="40" rx="12" fill="none" stroke="#fff" stroke-width="2.5"/><line x1="14" y1="10" x2="14" y2="18" stroke="#fff" stroke-width="2.5" stroke-linecap="round"/></svg>

<section class="about">
  <div class="about-img abs" role="img" aria-label="Two hands gripping and pulling through a broken wall"></div>
  <h2 class="head abs">About Us</h2>
  <p class="abs"><b>QUILLHORN ESCAPE GAME</b> is the heart pounding, code-cracking, mind-bending race against time experience that will require everyone in your group's collective intellect, ingenuity, and problem-solving skills to escape.</p>
  <div class="btn" style="left:613px;top:979px;width:110px;height:31px">Learn More</div>
</section>

<section class="rooms abs">
  <h2 class="head section-title abs" style="left:227px;top:70px">Find the Right Room for You</h2>
</section>
<div class="room abs" style="left:174px;top:1325px"><div class="shot" role="img" aria-label="Island prison at night" style="background:radial-gradient(ellipse at 50% 70%,#5a4a3a,#1c1e26 60%)">Iron Isle</div><svg width="30" height="207"><path d="M0 0H30V10H10V197H30V207H0Z" fill="#e3000f"/></svg></div>
<div class="room abs" style="left:468px;top:1325px"><div class="shot" role="img" aria-label="Dead forest at dusk" style="background:linear-gradient(#4a4a4a,#181818)">Apocalypse</div><svg width="30" height="207"><path d="M0 0H30V10H10V197H30V207H0Z" fill="#e3000f"/></svg></div>
<div class="room abs" style="left:763px;top:1325px"><div class="shot" role="img" aria-label="Foggy haunted cabin" style="background:linear-gradient(#5a5a5a,#2a2a2a);font-weight:400;font-size:30px;letter-spacing:2px">Haunted Cabin</div><svg width="30" height="207"><path d="M0 0H30V10H10V197H30V207H0Z" fill="#e3000f"/></svg></div>
<div class="room abs" style="left:174px;top:1572px"><div class="shot" role="img" aria-label="Dark asylum corridor" style="background:linear-gradient(#3a3a3a,#151515);font-weight:400;letter-spacing:4px">Asylum</div><svg width="30" height="207"><path d="M0 0H30V10H10V197H30V207H0Z" fill="#e3000f"/></svg></div>
<div class="room abs" style="left:468px;top:1572px"><div class="shot" role="img" aria-label="Gangster era alley with tommy gun" style="background:linear-gradient(#3f3a32,#121212)">Racketeer</div><svg width="30" height="207"><path d="M0 0H30V10H10V197H30V207H0Z" fill="#e3000f"/></svg></div>
<div class="room abs" style="left:763px;top:1572px"><div class="shot" role="img" aria-label="Horde of zombies in a dark street" style="background:linear-gradient(#3a3a3a,#161616);font-size:13px">View Details</div><svg width="30" height="207"><path d="M0 0H30V10H10V197H30V207H0Z" fill="#e3000f"/></svg></div>

<h2 class="head section-title abs center" style="left:0;top:1900px;width:1200px">Quillhorn Escape Game Prices</h2>
<div class="price abs" style="left:174px;top:2026px"><div class="tier">ADULTS</div><div class="amt">$ 28.99</div><ul><li>Rooms</li><li>Haunted Cabin</li><li>Dead Zone</li><li>Iron Isle</li><li>Asylum</li><li>Racketeer</li></ul><div class="btn" style="left:64px;top:322px;width:116px;height:30px">Book Now</div></div>
<div class="price abs" style="left:468px;top:2026px"><div class="tier">KIDS 6-12</div><div class="amt">$ 23.99</div><ul><li>Rooms</li><li>Haunted Cabin</li><li>Dead Zone</li><li>Iron Isle</li><li>Asylum</li><li>Racketeer</li></ul><div class="btn" style="left:64px;top:322px;width:116px;height:30px">Book Now</div></div>
<div class="price abs" style="left:763px;top:2026px"><div class="tier">5 AND UNDER</div><div class="amt">FREE</div><ul><li>Rooms</li><li>Haunted Cabin</li><li>Dead Zone</li><li>Iron Isle</li><li>Asylum</li><li>Racketeer</li></ul><div class="btn" style="left:64px;top:322px;width:116px;height:30px">Book Now</div></div>

<svg class="abs" style="left:140px;top:2505px" width="1060" height="310" viewBox="0 0 1060 310">
  <defs><linearGradient id="band" x1="0" x2="1"><stop offset="0" stop-color="#3a0004"/><stop offset=".55" stop-color="#b5000c"/><stop offset="1" stop-color="#e3000f"/></linearGradient></defs>
  <path d="M30 40 L1060 0 V270 L30 280Z" fill="url(#band)"/>
  <path d="M0 0 H170 V18 H18 V292 H170 V310 H0Z" fill="#e3000f"/>
  <circle cx="38" cy="152" r="5" fill="#fff"/>
</svg>
<h2 class="head abs center" style="left:0;top:2600px;width:1200px;font-size:54px">Upgrade to a Private Experience</h2>
<p class="abs center" style="left:300px;top:2682px;width:600px;font-size:14px;line-height:26px;font-weight:700">Multiple parties can book the same room. If you would like to book a private experience, please contact us by phone .</p>

<section class="benefits abs">
  <h2 class="head abs center" style="left:0;top:62px;width:1200px;font-size:54px;line-height:70px">Discover the Benefits<br>of Escape Rooms!</h2>
  <p class="abs center" style="left:0;top:214px;width:1200px;font-size:14px;font-weight:700">Escape rooms are fun, foster teamwork, and give you a sense of accomplishment.</p>
</section>

<div class="benefit abs" style="left:176px;top:3153px">
  <svg class="abs" width="150" height="250"><path d="M1 30 Q1 1 30 1 H120 Q149 1 149 30" fill="none" stroke="#aaa" stroke-dasharray="3 3"/><path d="M1 30 V190 Q1 249 75 249 Q149 249 149 190 V30" fill="none" stroke="#ddd" stroke-width="1.5"/><circle cx="1" cy="42" r="4" fill="#e3000f"/><circle cx="149" cy="42" r="4" fill="#e3000f"/><circle cx="75" cy="194" r="48" fill="#e3000f" stroke="#fff" stroke-width="3"/><g fill="none" stroke="#fff" stroke-width="2.5"><circle cx="75" cy="194" r="10"/><circle cx="57" cy="178" r="6"/><circle cx="93" cy="178" r="6"/><circle cx="57" cy="210" r="6"/><circle cx="93" cy="210" r="6"/></g></svg>
  <div class="label">Improve<b>Communication and Social Skills</b></div>
</div>
<div class="benefit abs" style="left:350px;top:3153px">
  <svg class="abs" width="150" height="250"><path d="M1 30 Q1 1 30 1 H120 Q149 1 149 30" fill="none" stroke="#aaa" stroke-dasharray="3 3"/><path d="M1 30 V190 Q1 249 75 249 Q149 249 149 190 V30" fill="none" stroke="#ddd" stroke-width="1.5"/><circle cx="1" cy="42" r="4" fill="#e3000f"/><circle cx="149" cy="42" r="4" fill="#e3000f"/><circle cx="75" cy="194" r="48" fill="#e3000f" stroke="#fff" stroke-width="3"/><g fill="none" stroke="#fff" stroke-width="2.5"><circle cx="75" cy="194" r="16"/><circle cx="75" cy="194" r="6"/><path d="M75 172v-6M75 216v6M53 194h-6M97 194h6"/></g></svg>
  <div class="label">Challenge Your<b>Creative Thinking and Problem Solving Skills</b></div>
</div>
<div class="benefit abs" style="left:525px;top:3153px">
  <svg class="abs" width="150" height="250"><path d="M1 30 Q1 1 30 1 H120 Q149 1 149 30" fill="none" stroke="#aaa" stroke-dasharray="3 3"/><path d="M1 30 V190 Q1 249 75 249 Q149 249 149 190 V30" fill="none" stroke="#ddd" stroke-width="1.5"/><circle cx="1" cy="42" r="4" fill="#e3000f"/><circle cx="149" cy="42" r="4" fill="#e3000f"/><circle cx="75" cy="194" r="48" fill="#e3000f" stroke="#fff" stroke-width="3"/><g fill="none" stroke="#fff" stroke-width="2.5"><circle cx="75" cy="192" r="18"/><circle cx="75" cy="192" r="10"/><circle cx="75" cy="192" r="3"/></g></svg>
  <div class="label">Enhance and<b>Build Your Memory</b></div>
</div>
<div class="benefit abs" style="left:700px;top:3153px">
  <svg class="abs" width="150" height="250"><path d="M1 30 Q1 1 30 1 H120 Q149 1 149 30" fill="none" stroke="#aaa" stroke-dasharray="3 3"/><path d="M1 30 V190 Q1 249 75 249 Q149 249 149 190 V30" fill="none" stroke="#ddd" stroke-width="1.5"/><circle cx="1" cy="42" r="4" fill="#e3000f"/><circle cx="149" cy="42" r="4" fill="#e3000f"/><circle cx="75" cy="194" r="48" fill="#e3000f" stroke="#fff" stroke-width="3"/><g fill="none" stroke="#fff" stroke-width="2.5"><circle cx="62" cy="196" r="13"/><circle cx="88" cy="196" r="13"/></g></svg>
  <div class="label">Improve<b>Your Mood</b></div>
</div>
<div class="benefit abs" style="left:875px;top:3153px">
  <svg class="abs" width="150" height="250"><path d="M1 30 Q1 1 30 1 H120 Q149 1 149 30" fill="none" stroke="#aaa" stroke-dasharray="3 3"/><path d="M1 30 V190 Q1 249 75 249 Q149 249 149 190 V30" fill="none" stroke="#ddd" stroke-width="1.5"/><circle cx="1" cy="42" r="4" fill="#e3000f"/><circle cx="149" cy="42" r="4" fill="#e3000f"/><circle cx="75" cy="194" r="48" fill="#e3000f" stroke="#fff" stroke-width="3"/><path d="M75 172 L98 212 H52Z" fill="none" stroke="#fff" stroke-width="3" stroke-linejoin="round"/><path d="M75 186v12" stroke="#fff" stroke-width="3"/><circle cx="75" cy="204" r="2" fill="#fff"/></svg>
  <div class="label">Increase Your<b>Attention to Detail</b></div>
</div>

<div class="brand abs" style="left:0;top:3440px;width:1200px;justify-content:center;font-size:52px"><i style="width:12px;height:12px"></i>Quillhorn</div>
<p class="abs center" style="left:0;top:3524px;width:1200px;font-size:13px;font-weight:700;text-transform:uppercase">Visit Quillhorn Escape Game_ Today in Nashville or Pigeon Forge</p>

<section class="locations abs" role="img" aria-label="Shadowy hands pressing against frosted glass"></section>
<h2 class="head section-title abs center" style="left:0;top:3675px;width:1200px">Find Our Locations</h2>
<div class="loc abs" style="left:185px;top:3812px">
  <div class="brand"><i style="width:11px;height:11px"></i>Quillhorn</div>
  <div class="city">Nashville</div>
  <p>Wheelchair Accessible Rooms at Nashville: Asylum</p>
</div>
<div class="btn" style="left:324px;top:4013px;width:130px;height:32px">Book Now</div>
<div class="loc abs" style="left:598px;top:3812px">
  <div class="brand"><i style="width:11px;height:11px"></i>Quillhorn</div>
  <div class="city">Pigeon Forge</div>
  <p>Wheelchair Accessible Rooms at Pigeon Forge:<br>Racketeer, Haunted Cabin, Asylum</p>
</div>
<div class="btn" style="left:737px;top:4013px;width:130px;height:32px">Book Now</div>

<svg class="abs" style="left:145px;top:4160px" width="260" height="450"><path d="M0 0 H260 V30 H30 V420 H260 V450 H0Z" fill="#e3000f"/></svg>
<div class="who-panel abs"></div>
<h2 class="head abs center" style="left:0;top:4212px;width:1200px;font-size:54px">Quillhorn Who</h2>
<svg class="abs" style="left:186px;top:4385px" width="20" height="34"><path d="M18 2 L3 17 L18 32" fill="none" stroke="#fff" stroke-width="2"/></svg>
<svg class="abs" style="left:1000px;top:4385px" width="20" height="34"><path d="M2 2 L17 17 L2 32" fill="none" stroke="#fff" stroke-width="2"/></svg>

<div class="who-item abs" style="left:218px;top:4300px">
  <div class="icon-badge"><svg width="56" height="56" fill="none" stroke="#fff" stroke-width="2.5"><circle cx="28" cy="16" r="7"/><circle cx="12" cy="28" r="5"/><circle cx="44" cy="28" r="5"/><path d="M14 50 Q28 30 42 50"/><path d="M4 44 Q12 34 20 42M52 44 Q44 34 36 42"/></svg></div>
  <h4>Team Building</h4><p>What better way to foster synergy and teamwork than to be locked in a room together?</p>
</div>
<div class="who-item abs" style="left:485px;top:4300px">
  <div class="icon-badge"><svg width="56" height="56" fill="none" stroke="#fff" stroke-width="2.5"><path d="M10 18 H46 Q54 18 54 34 Q54 46 46 44 L40 36 H16 L10 44 Q2 46 2 34 Q2 18 10 18Z"/><path d="M15 27v8M11 31h8"/><circle cx="38" cy="28" r="2"/><circle cx="43" cy="33" r="2"/></svg></div>
  <h4>Gamers</h4><p>Have you been looking for a way to impress your friends with your amazing</p>
</div>
<div class="who-item abs" style="left:750px;top:4300px">
  <div class="icon-badge"><svg width="56" height="56" fill="none" stroke="#fff" stroke-width="2.5"><path d="M28 22 Q22 8 12 14 Q4 22 28 40 Q52 22 44 14 Q34 8 28 22Z"/><circle cx="16" cy="38" r="5"/><circle cx="40" cy="38" r="5"/><path d="M8 54 Q16 42 24 54M32 54 Q40 42 48 54"/></svg></div>
  <h4>Friends and Family</h4><p>Bring your family, friends, neighbors, or a stranger you just met, and join us</p>
</div>

<footer class="footer abs" role="img" aria-label="Faint dark figure behind the footer"></footer>
<div class="brand abs" style="left:174px;top:4708px;font-size:50px"><i style="width:12px;height:12px"></i>Quillhorn</div>
<div class="abs" style="left:925px;top:4731px;display:flex;gap:18px">
  <div class="social">f</div><div class="social">t</div><div class="social">in</div>
</div>
<div class="abs" style="left:174px;top:4775px;width:854px;height:1px;background:#333"></div>
<div class="f-title abs" style="left:174px;top:4798px"><span>Q</span>UICK <span>L</span>INKS</div>
<ul class="f-links abs" style="left:174px;top:4842px"><li>Home</li><li>About Us</li><li>Escape Rooms</li><li>FAQ</li></ul>
<ul class="f-links abs" style="left:324px;top:4842px"><li>Gallery</li><li>Gift Cards</li><li>Contact</li></ul>
<div class="f-title abs" style="left:557px;top:4798px"><span>C</span>ONTACT <span>I</span>NFO</div>
<div class="f-contact abs" style="left:557px;top:4850px;width:220px">
  <div><svg width="12" height="16"><path d="M6 15 Q0 8 0 6 A6 6 0 0 1 12 6 Q12 8 6 15Z" fill="#e3000f"/><circle cx="6" cy="6" r="2" fill="#111"/></svg><span>1180 Harlow Lane, Nashville, TN 37204</span></div>
  <div><svg width="12" height="14"><path d="M2 1 L5 1 L6 5 L4 6 Q6 10 8 11 L9 9 L12 10 L12 13 Q5 14 1 4Z" fill="#e3000f"/></svg><span>629-555-0148</span></div>
  <div><svg width="13" height="10"><rect width="13" height="10" fill="#e3000f"/><path d="M0 0 L6.5 5 L13 0" fill="none" stroke="#111"/></svg><span>nashville@quillhornpuzzles.com</span></div>
</div>
<div class="f-contact abs" style="left:830px;top:4850px;width:210px">
  <div><svg width="12" height="16"><path d="M6 15 Q0 8 0 6 A6 6 0 0 1 12 6 Q12 8 6 15Z" fill="#e3000f"/><circle cx="6" cy="6" r="2" fill="#111"/></svg><span>740 Ridgeview Way, Suite 9, Pigeon Forge, TN 37863</span></div>
  <div><svg width="12" height="14"><path d="M2 1 L5 1 L6 5 L4 6 Q6 10 8 11 L9 9 L12 10 L12 13 Q5 14 1 4Z" fill="#e3000f"/></svg><span>865-555-0172</span></div>
  <div><svg width="13" height="10"><rect width="13" height="10" fill="#e3000f"/><path d="M0 0 L6.5 5 L13 0" fill="none" stroke="#111"/></svg><span>info@quillhornpuzzles.com</span></div>
</div>
<div class="abs" style="left:174px;top:5040px;width:854px;height:1px;background:#333"></div>
<p class="abs" style="left:174px;top:5057px;font-size:10px;color:#999">© 2022 <span style="color:#e3000f">QUILLHORN ESCAPE GAME</span>. All right reserved</p>
<svg class="abs" style="left:984px;top:5046px" width="40" height="40"><circle cx="20" cy="20" r="20" fill="#e3000f"/><path d="M20 29V12M13 18L20 11L27 18" fill="none" stroke="#fff" stroke-width="2.5"/></svg>

</body>
</html>
```